WP website design for Dorrance

We need a wordpress design that will incorporate a professional color scheme with company logo in a clean layout. The design needs to consider that this will be developed on a responsive theme. Colors are will be the green of the logo and any others that will creatively highlight it.

Industry/Entity Type

It Company

Font styles to use
Sans Serif

Requirements
Must have
• Navigation: 1) Home 2) Auctions 3) Auction Services 4) Sellers 5) KT Dorrance Livestock 6) About Us 7) Contact Us
Site will have slideshow element, image attached.
Widgets will be: 1)Email Signup form 2) Featured Auctions widget 3) Social Media (FB, Youtube, RSS) 4) News & Events blog
Footer will have smaller company logo, association logos (attached) and contact info (below)
▪ K.T. Dorrance Inc. / Auctioneers
▪ 4715 NC Hwy 91
▪ Belmora, NC 27640
▪ Office: (252) 555-0187
▪ Cell: (252) 555-0163
▪ email: ktdorrance@ktdorrance-example.com
Nice to have
• Site will have drop-down menus - please indicate the styling, for instance the dropdown menus

```html
<!DOCTYPE html>
<html lang="en">
<head>
<meta charset="utf-8">
<title>K.T. Dorrance Inc. / Auctioneers</title>
<link rel="stylesheet" href="https://fonts.googleapis.com/css2?family=Arimo:wght@400;700&display=swap">
<style>
:root{
  --green:#4a9a1e;
  --green-dark:#2f7a10;
  --green-light:#5fb92c;
  --nav-active:#3a7a1f;
  --text:#333;
  --muted:#666;
  --rule:#d4d4d4;
  --panel:#f1f1f1;
  --footer:#e8e8e8;
  --black:#1e1e1e;
}
*{box-sizing:border-box;margin:0;padding:0}
html,body{width:813px;height:1200px;overflow:hidden;background:#fff;font-family:"Arimo",Arial,sans-serif;color:var(--text)}
.page{position:relative;width:813px;height:1200px}
.abs{position:absolute}
.topline{left:0;top:0;width:813px;height:4px;background:#111}
.brand{left:116px;top:30px;color:var(--green);font-size:13px;line-height:16px}
.brand .mark{display:inline-block;width:14px;height:14px;border-radius:50%;background:var(--green);vertical-align:-2px;margin-right:6px}
.brand small{display:block;font-size:9px;color:var(--green);margin-left:20px}
.phone{left:476px;top:35px;font-size:11.5px;color:#333;display:flex;align-items:center;gap:5px}
.search{left:576px;top:30px;width:122px;height:24px;background:#ebebeb;border:1px solid #ddd;font-size:7px;color:#555;padding:8px 0 0 9px}
.search svg{position:absolute;right:7px;top:6px}
.nav{left:0;top:81px;width:813px;height:45px;background:linear-gradient(#5cb82a,#3f9119);display:flex;padding-left:116px}
.nav a{color:#fff;font-size:10px;text-decoration:none;padding:0 18px;line-height:45px;border-right:1px solid rgba(255,255,255,.18)}
.nav a.active{background:var(--nav-active)}
.nav a:last-child{border-right:none}
.hero{left:0;top:126px;width:813px;height:347px;background:linear-gradient(#bfc7cd 0%,#8a8a6e 25%,#9b6a3a 42%,#8c6a44 52%,#5e5a4a 70%,#8e8c84 100%)}
.hero h1{position:absolute;left:0;width:813px;top:110px;text-align:center;color:#fff;font-size:19px;font-weight:700;text-shadow:0 1px 3px rgba(0,0,0,.6)}
.hero p{position:absolute;left:0;width:813px;top:146px;text-align:center;color:#fff;font-size:12px;font-weight:700;text-shadow:0 1px 3px rgba(0,0,0,.6)}
.hero .btn{position:absolute;left:347px;top:181px;width:115px;height:32px;border:2px solid #fff;border-radius:3px;color:#fff;font-size:14px;text-align:center;line-height:28px;text-shadow:0 1px 2px rgba(0,0,0,.5)}
.hero .arrow{position:absolute;top:147px;width:26px;height:26px;border-radius:50%;background:rgba(255,255,255,.7)}
.section-title{color:var(--green);font-size:14px}
.pager{display:flex;gap:1px}
.pager span{width:12px;height:12px;background:#666;display:block;position:relative}
.pager svg{position:absolute;left:3px;top:2px}
.featured-rule{left:116px;top:532px;width:583px;height:1px;background:var(--rule)}
.thumb{top:542px;width:140px;height:91px;border-radius:3px}
.caption{top:644px;width:140px;text-align:center;font-size:10.5px;color:#444}
.about{left:0;top:684px;width:813px;height:204px;background:var(--panel);border-top:1px solid #e2e2e2;border-bottom:2px solid #e0e0e0}
.about h2{position:absolute;left:116px;top:20px;color:var(--green);font-size:14px;font-weight:400}
.about .copy{position:absolute;left:116px;top:45px;width:436px;font-size:8.3px;line-height:13.6px;color:#222}
.about .copy p{margin-bottom:13px}
.portrait{position:absolute;left:569px;top:17px;width:122px;height:142px;background:#fff;border:1px solid #bbb;padding:3px;box-shadow:0 1px 3px rgba(0,0,0,.2)}
.portrait div{width:100%;height:100%;background:linear-gradient(#3d4a2a,#8a8e7a 45%,#d8d8d6 70%,#6a5a48)}
.card{background:linear-gradient(#fafafa,#e9e9e9);border:1px solid #d0d0d0}
.card h3{color:var(--green);font-size:9px;font-weight:400}
.card p{font-size:6.6px;line-height:11.7px;color:#666}
.footer{left:0;top:1032px;width:813px;height:114px;background:var(--footer)}
.footer h4{position:absolute;top:19px;color:var(--green);font-size:9.5px;font-weight:400}
.footer .small{font-size:6.8px;line-height:10px;color:#555}
.bottom{left:0;top:1146px;width:813px;height:54px;background:var(--black);color:#ddd;font-size:8px}
</style>
</head>
<body>
<div class="page">
  <div class="abs topline"></div>

  <div class="abs brand"><span class="mark"></span>K.T. Dorrance<small>Inc. / Auctioneers</small></div>

  <div class="abs phone">
    <svg width="12" height="12" viewBox="0 0 12 12"><rect width="12" height="12" rx="2" fill="#3f9119"/><path d="M3.5 2.8l1.4 1.6-.7.9c.5 1 1.3 1.8 2.3 2.3l.9-.7 1.6 1.4-.9 1c-2.7-.4-4.9-2.6-5.3-5.3z" fill="#fff"/></svg>
    (252) 555-0187
  </div>
  <div class="abs search">Search...
    <svg width="11" height="11" viewBox="0 0 11 11"><circle cx="4.5" cy="4.5" r="3.3" fill="none" stroke="#777" stroke-width="1.5"/><path d="M7 7l3 3" stroke="#777" stroke-width="1.7"/></svg>
  </div>

  <nav class="abs nav">
    <a class="active" href="#">Home</a>
    <a href="#">Auctions</a>
    <a href="#">Auction Services</a>
    <a href="#">Sellers</a>
    <a href="#">KT Dorrance Livestock</a>
    <a href="#">About Us</a>
    <a href="#">Contact Us</a>
  </nav>

  <section class="abs hero" role="img" aria-label="Slideshow photo of an autumn farm pond with trees reflected in the water">
    <h1>NORTH CAROLINA AUCTIONS AND AUCTIONEERING</h1>
    <p>LOREM IPSUM IS SIMPLY DUMMY TEXT OF THE PRINTING AND TYPESETTING</p>
    <div class="btn">More Details</div>
    <div class="arrow" style="left:60px"><svg width="26" height="26" viewBox="0 0 26 26"><path d="M15 7l-6 6 6 6" fill="none" stroke="#666" stroke-width="1.6"/></svg></div>
    <div class="arrow" style="left:726px"><svg width="26" height="26" viewBox="0 0 26 26"><path d="M11 7l6 6-6 6" fill="none" stroke="#666" stroke-width="1.6"/></svg></div>
  </section>

  <h2 class="abs section-title" style="left:117px;top:508px;font-weight:400">Featured Auctions</h2>
  <div class="abs pager" style="left:672px;top:512px">
    <span><svg width="6" height="8"><path d="M5 0L1 4l4 4" fill="none" stroke="#fff"/></svg></span>
    <span><svg width="6" height="8"><path d="M1 0l4 4-4 4" fill="none" stroke="#fff"/></svg></span>
  </div>
  <div class="abs featured-rule"></div>

  <div class="abs thumb" style="left:117px;background:linear-gradient(#7fa36a,#3c8a2a 55%,#5b6d3a)" role="img" aria-label="Green grain drill farm implement"></div>
  <div class="abs thumb" style="left:263px;background:linear-gradient(#5f7d4a,#2e2e26 50%,#7a9a52)" role="img" aria-label="Cow and calf in a pasture"></div>
  <div class="abs thumb" style="left:410px;background:linear-gradient(#c9d2d8,#b8bcbd 50%,#7b8a5a)" role="img" aria-label="Aluminium livestock trailer"></div>
  <div class="abs thumb" style="left:556px;background:linear-gradient(#8aa27a,#3f7a2a 50%,#6a7a4a)" role="img" aria-label="Green farm tractor"></div>
  <div class="abs caption" style="left:117px">DALE WHITMORE</div>
  <div class="abs caption" style="left:268px">DALE WHITMORE</div>
  <div class="abs caption" style="left:407px">DALE WHITMORE</div>
  <div class="abs caption" style="left:560px">DALE WHITMORE</div>

  <section class="abs about">
    <h2>North Carolina Auctions and Auctioneering</h2>
    <div class="copy">
      <p>Our auction business was started in 1977. We conduct farm equipment, logging &amp; industrial equipment, real estate, antique &amp; cattle sales.</p>
      <p>K. T. Dorrance, owner/president, was raised on the family farm in Belmora County. This farm has been in his family since 1916. The office for the auction business is also located at this farm.</p>
      <p>There were many family values passed on to him which are used in everyday life. Some of these are used in the auction business today. For example - (1) give a man a fair measure (2) look a person straight in the eye &amp; give them a firm hand shake. When you employ K. T. Dorrance Inc./Auctioneers you are dealing with a company known for treating their customers, whether a seller or buyer, with these values.</p>
    </div>
    <div class="portrait"><div role="img" aria-label="Photo of the owner on horseback"></div></div>
  </section>

  <h2 class="abs section-title" style="left:116px;top:907px;font-size:11px;font-weight:400">EVENTS BLOG</h2>
  <div class="abs pager" style="left:458px;top:907px">
    <span><svg width="6" height="8"><path d="M5 0L1 4l4 4" fill="none" stroke="#fff"/></svg></span>
    <span><svg width="6" height="8"><path d="M1 0l4 4-4 4" fill="none" stroke="#fff"/></svg></span>
  </div>
  <div class="abs card" style="left:115px;top:927px;width:371px;height:81px">
    <div class="abs" style="left:14px;top:10px;width:77px;height:58px;background:linear-gradient(#9ab07a,#3a3a34 50%,#6f9a4a)" role="img" aria-label="Black cow standing in grass"></div>
    <h3 class="abs" style="left:98px;top:12px">Auction and Auctioneering</h3>
    <p class="abs" style="left:99px;top:26px;width:260px">Lorem Ipsum is simply dummy text of the printing and typesetting industry. Lorem Ipsum has been the industry's standard dummy text ever since the 1500s, when an unknown printer took a galley of type and scrambled</p>
  </div>

  <h2 class="abs section-title" style="left:494px;top:908px;font-size:11px;font-weight:400">NEWS</h2>
  <div class="abs pager" style="left:672px;top:907px">
    <span><svg width="6" height="8"><path d="M5 0L1 4l4 4" fill="none" stroke="#fff"/></svg></span>
    <span><svg width="6" height="8"><path d="M1 0l4 4-4 4" fill="none" stroke="#fff"/></svg></span>
  </div>
  <div class="abs card" style="left:494px;top:926px;width:204px;height:81px">
    <div class="abs" style="left:6px;top:9px;width:31px;height:32px;background:#fff;border:1px solid #ccc;text-align:center">
      <div style="font-size:10px;font-weight:700;margin-top:5px">20</div>
      <div style="font-size:5.5px;color:#888;margin-top:3px">mar</div>
    </div>
    <h3 class="abs" style="left:43px;top:8px;font-size:8.5px">Lorem Ipsum is simply dummy text</h3>
    <p class="abs" style="left:43px;top:21px;width:156px">Lorem Ipsum is simply dummy text of the printing and typesetting industry. Lorem Ipsum has been the industry's standard dummy text ever since the 1500s, when an unknown printer took a galley of</p>
  </div>

  <footer class="abs footer">
    <h4 style="left:116px">Our Company</h4>
    <div class="abs" style="left:116px;top:39px;width:62px;height:38px;background:#fff;color:var(--green);font-size:7px;line-height:9px;padding:9px 4px">K.T. Dorrance Inc. / Auctioneers</div>

    <h4 style="left:224px">Contact info</h4>
    <div class="abs small" style="left:225px;top:42px">4715 NC Hwy 91<br>Belmora, NC 27640<br>
      <div style="height:7px"></div>(252) 555-0163 K.T.'s mobile<br>ktdorrance@ktdorrance-example.com</div>

    <h4 style="left:383px">Association</h4>
    <div class="abs" style="left:383px;top:37px;width:145px;height:45px;background:#fff;display:flex;align-items:center;justify-content:space-around">
      <div style="width:50px;height:16px;background:#555;border-radius:3px" role="img" aria-label="Auctioneers association badge"></div>
      <div style="width:32px;height:24px;background:#c0392b;border-radius:3px" role="img" aria-label="Beef industry badge"></div>
      <div style="width:32px;height:32px;background:#3a7a3a;border-radius:50%" role="img" aria-label="Cattlemen association badge"></div>
    </div>

    <h4 style="left:562px">Email Signup</h4>
    <div class="abs" style="left:563px;top:39px;width:135px;height:23px;background:#fff;border:2px solid #cfcfcf;font-size:8px;color:#777;padding:5px 0 0 9px">Enter Your Email Address</div>
    <div class="abs" style="left:562px;top:70px;width:49px;height:19px;border-radius:3px;background:linear-gradient(var(--green-light),var(--green-dark));color:#fff;font-size:8px;font-weight:700;text-align:center;line-height:19px">Sign Up</div>
  </footer>

  <div class="abs bottom">
    <div class="abs" style="left:117px;top:23px">© Copyright 2014 &nbsp;. All Rights Reserved</div>
    <div class="abs" style="left:643px;top:17px;display:flex;gap:4px">
      <span style="width:16px;height:16px;border-radius:50%;background:#fff;display:block" role="img" aria-label="Social network link"></span>
      <span style="width:16px;height:16px;border-radius:50%;background:#fff;display:block" role="img" aria-label="RSS feed link"></span>
      <span style="width:16px;height:16px;border-radius:50%;background:#fff;display:block" role="img" aria-label="Video channel link"></span>
    </div>
  </div>
</div>
</body>
</html>
```